Wine Bottle Label for the brand Gliding Heron for a Sherry wine

A wine label for a Dry Sherry. We want it consistent with existing Gliding Heron and Quiet Otter labeling. It should say "Quiet Otter Sherry" We want a very retro look similar to the attached labels which are from our core wines. The sherry is a side project that fits into the 'quiet otter' series (label included). We would like a lot of the similar label structure to the existing quiet otter label, but with a different caricature of the fox. We have had one that we did in Copper ridge bourbon barrels and the caricature was of a buffalo with a barrel imbibing. We have also had a giraffe on a skin contact white. I have included the mural and other logos throughout the project to give you a sense of the previous work we have done.

Industry/Entity Type

Winemaking, wine labels

Requirements
Must have
• Quiet Otter elements

```html
<!DOCTYPE html>
<html lang="en">
<head>
<meta charset="utf-8">
<title>Quiet Otter Sherry – Label</title>
<link href="https://fonts.googleapis.com/css2?family=Staatliches&family=Oswald:wght@300;400&display=swap" rel="stylesheet">
<style>
  :root {
    --backdrop: #1a1a1c;
    --label-edge: #d8d2e4;
    --paper: #fbfbfa;
    --sherry-red: #e5412c;
    --ink-dark: #3d3a40;
    --ink-purple: #8a5a9c;
    --art-tone: #f2c7bd;
  }
  * { margin: 0; padding: 0; box-sizing: border-box; }
  html, body { width: 1200px; height: 1200px; overflow: hidden; background: var(--backdrop); }
  .label {
    position: absolute; left: 240px; top: 60px; width: 720px; height: 1080px;
    background: var(--label-edge);
  }
  .label__paper {
    position: absolute; inset: 14px; background: var(--paper);
  }
  .label__frame { position: absolute; inset: 0; }
  .title {
    position: absolute; left: 0; right: 0; top: 80px; text-align: center;
    font-family: "Staatliches", sans-serif; color: var(--sherry-red);
    line-height: 0.92;
  }
  .title__brand { display: block; font-size: 122px; letter-spacing: 4px; }
  .title__kind { display: block; font-size: 138px; letter-spacing: 6px; }
  .origin {
    position: absolute; left: 0; right: 0; top: 350px; text-align: center;
    font-family: "Oswald", sans-serif; font-weight: 300; color: var(--ink-dark);
    white-space: nowrap;
  }
  .origin__small { font-size: 14px; text-transform: uppercase; }
  .origin__lead { border-bottom: 1.5px solid var(--ink-purple); padding-bottom: 3px; }
  .origin__main { font-size: 31px; font-weight: 400; text-transform: uppercase; }
  .origin__winery { font-size: 31px; color: var(--ink-purple); text-transform: uppercase; }
  .mascot-art {
    position: absolute; left: 215px; top: 440px; width: 290px; height: 520px;
    background: radial-gradient(ellipse at 50% 45%, var(--art-tone) 0%, rgba(242,199,189,0.35) 60%, rgba(242,199,189,0) 75%);
  }
  .spec {
    position: absolute; top: 800px; width: 110px; text-align: center;
    font-family: "Oswald", sans-serif; color: var(--ink-dark); line-height: 1.05;
    text-transform: uppercase;
  }
  .spec--volume { left: 52px; }
  .spec--strength { right: 52px; color: var(--sherry-red); }
  .spec__label { font-size: 30px; font-weight: 300; }
  .spec__value { font-size: 52px; font-weight: 400; }
</style>
</head>
<body>
  <div class="label">
    <div class="label__paper"></div>
    <svg class="label__frame" width="720" height="1080" viewBox="0 0 720 1080">
      <path d="M64 28 H656 A36 36 0 0 0 692 64 V1016 A36 36 0 0 0 656 1052 H64 A36 36 0 0 0 28 1016 V64 A36 36 0 0 0 64 28 Z"
            fill="none" stroke="var(--sherry-red)" stroke-width="4"/>
      <path d="M68 36 H652 A40 40 0 0 0 684 68 V1012 A40 40 0 0 0 652 1044 H68 A40 40 0 0 0 36 1012 V68 A40 40 0 0 0 68 36 Z"
            fill="none" stroke="var(--sherry-red)" stroke-width="1.2"/>
    </svg>

    <h1 class="title">
      <span class="title__brand">Quiet Otter</span>
      <span class="title__kind">Sherry</span>
    </h1>

    <p class="origin">
      <span class="origin__small origin__lead">Of the famous</span>
      <span class="origin__main">Gliding Heron Vineyard</span>
      <span class="origin__small">and</span>
      <span class="origin__winery">Winery</span>
    </p>

    <div class="mascot-art" role="img" aria-label="Engraved-style caricature of a standing otter in a coat holding a bottle"></div>

    <div class="spec spec--volume">
      <div class="spec__label">Vol.</div>
      <div class="spec__value">500</div>
      <div class="spec__label">ml</div>
    </div>
    <div class="spec spec--strength">
      <div class="spec__label">Alc</div>
      <div class="spec__value">13%</div>
      <div class="spec__label">by vol</div>
    </div>
  </div>
</body>
</html>
```